Equine Horse Employment site

We need to redesign the layout of Stablemark Hire.co.uk

It will offer Job seekers and Employers the place to look for a job, and look for a candidate.

The logical format needs to be improved and the layout must look highly visually appealing.

It needs to be incredibly simple to use and one click access to any part of the site.

The homepage must convey the following

- Log in and register areas
- Current Job Listings
- Current CV's
- Exclusive Service Club button
- Search box to allow simple searching for Jobs or CVs

We need PSD layouts for Homepage, Job listing Page, CV listing Page, Job Profile and CV Profile. This job is for the design of 5 PSD screens.

Generic page for ancillary page such as about, contact and news.

The biggest competitor is PaddockPost.com

Please ask us any questions and please be prepared to make changes, as we are very particular.

More work will be provided to the winning designer.

thanks

• It must not look cheap or like a job board, it has to have character and feel friendly, and inviting. Please do not submit poor designs that look like a job board, as they will be rejected instantly.

thanks

```html
<!DOCTYPE html>
<html lang="en">
<head>
<meta charset="utf-8">
<title>Stablemark Hire – Equestrian Recruitment</title>
<link href="https://fonts.googleapis.com/css2?family=Roboto:wght@400;500;700&family=Oswald:wght@500;600&family=Cinzel:wght@400;600&family=Titan+One&display=swap" rel="stylesheet">
<style>
:root{
  --page:#f4f4f4;
  --ink:#333;
  --muted:#555;
  --brand:#1d5fa8;
  --sky:#2ea3dc;
  --sky-deep:#1a86c4;
  --orange:#f25a17;
  --yellow:#f6e21a;
  --banner-dark:#3b6b12;
  --banner-lime:#9cc91e;
  --cyan:#1e8ac8;
  --btn-blue:#2d7fbf;
  --footer-top:#565656;
  --footer-bottom:#000;
  --footer-link:#b7b7b7;
  --line:#cfcfcf;
}
*{box-sizing:border-box;margin:0;padding:0}
html,body{width:894px;height:1200px;overflow:hidden}
body{background:var(--page);font-family:Roboto,Arial,sans-serif;color:var(--ink);position:relative}
.abs{position:absolute}
a{color:inherit}

/* header */
.greeting{left:650px;top:8px;font-size:13px;font-weight:700;color:var(--brand)}
.account{left:740px;top:11px;font-size:10.5px;font-weight:500;color:#444}
.account span{margin:0 4px;color:#777}
.brand{left:64px;top:58px}
.brand-name{font-family:Cinzel,serif;font-size:21px;font-weight:400;color:#1c2a3a;letter-spacing:.5px;display:flex;align-items:center;gap:8px;white-space:nowrap}
.brand-mark{width:14px;height:14px;background:#d7442b;display:inline-block}
.brand-tag{font-size:7.5px;color:#b0261c;margin:3px 0 0 30px}
.promo{left:349px;top:31px;width:477px;height:58px;background:var(--banner-dark);font-family:Cinzel,serif;color:#fff;overflow:hidden}
.promo-main{position:absolute;left:9px;top:8px;font-size:15.5px;white-space:nowrap}
.promo-sponsor{position:absolute;right:9px;top:9px;font-size:7px;line-height:9px;text-align:right;white-space:nowrap}
.promo-strip{position:absolute;left:0;right:0;bottom:8px;height:15px;background:var(--banner-lime);color:#2b3d06;font-size:10px;text-align:center;line-height:15px;white-space:nowrap}
.nav{right:68px;top:100px;font-size:10.5px;font-weight:700;color:#444;display:flex;gap:6px}
.nav .sep{color:#777;font-weight:400}
.nav .current{border-bottom:2px solid var(--sky);padding-bottom:2px}

/* hero */
.hero{left:0;top:122px;width:894px;height:348px;background:radial-gradient(ellipse at 62% 30%,#48bdea 0%,var(--sky) 45%,var(--sky-deep) 100%)}
.hero-art{left:0;top:0;width:894px;height:348px}
.welcome{left:66px;top:117px;width:350px;font-size:16.5px;font-weight:700;color:#fff;line-height:22.5px}
.club-btn{left:64px;top:222px;width:277px;height:34px;background:linear-gradient(#ff7a33,var(--orange));border:1px solid #fff;border-radius:3px;color:#fff;font-family:"Titan One",sans-serif;font-size:12.5px;letter-spacing:.5px;line-height:32px;text-align:center}
.search-title{left:450px;top:63px;font-family:"Titan One",sans-serif;font-size:23px;color:#fff;letter-spacing:.5px}
.search-tabs{right:68px;top:96px;font-size:24px;font-weight:700;font-style:italic;color:var(--yellow)}
.search-tabs span{margin:0 10px}
.search-field{left:446px;top:148px;width:380px;height:47px;background:#fff;border-radius:24px;box-shadow:0 2px 3px rgba(0,0,0,.3)}
.search-field svg{position:absolute;left:14px;top:8px}
.search-field .placeholder{position:absolute;left:53px;top:13px;font-size:18px;font-weight:500;color:#333}
.employer{left:458px;top:205px;font-size:13px;color:#fff}
.show-all{left:458px;top:235px;font-size:13px;color:#fff;text-decoration:underline}
.search-btn{left:746px;top:208px;width:80px;height:30px;background:linear-gradient(#ff7a33,var(--orange));border:1px solid #fff;border-radius:4px;color:#fff;font-size:17px;text-align:center;line-height:28px}
.adv-search{left:738px;top:246px;font-size:10px;font-weight:500;color:#fff;text-decoration:underline}
.slider{left:385px;top:459px;width:120px;height:28px;background:#f4f4f4;border:1px solid #ccc;border-radius:3px}

/* about */
.about-title{left:64px;top:498px;font-family:Oswald,sans-serif;font-size:19px;font-weight:600;color:#222}
.about-text{left:64px;top:538px;width:762px;font-size:9.2px;line-height:18px;color:var(--muted);letter-spacing:-.25px}
.about-text p{margin-bottom:18px}

/* panels */
.panels{left:64px;top:662px;width:762px;height:274px;background:#fff;border:1px solid var(--line)}
.divider{top:12px;width:1px;height:250px;background:var(--line)}
.col-title{font-family:Oswald,sans-serif;font-size:18px;font-weight:600;color:#222;letter-spacing:-.3px}
.col-title .hl{color:var(--cyan)}
.job{margin-top:12px}
.job h3{font-size:17px;font-weight:400;color:#111}
.job p{font-size:8.6px;line-height:13.5px;color:#222}
.cv p{font-size:8.6px;line-height:13.5px;color:#222;margin-top:10px;width:200px}
.listings{list-style:none;margin-top:10px}
.listings li{font-size:8.8px;color:#222;height:22.4px;display:flex;align-items:flex-start;gap:7px}
.more{width:57px;height:24px;background:linear-gradient(#4b9cd6,var(--btn-blue));border-radius:8px;color:#fff;font-size:10.5px;font-weight:700;text-align:center;line-height:24px;border:1px solid #1f6aa5}

/* footer */
.footer{left:0;top:969px;width:894px;height:231px;background:linear-gradient(var(--footer-top),var(--footer-bottom) 85%)}
.f-title{font-size:13px;color:#fff}
.f-links{list-style:none;font-size:10px;color:var(--footer-link);line-height:17.8px}
.join-input{left:592px;top:1017px;width:170px;height:24px;background:#fff;border:1px solid #999}
.signup{left:770px;top:1017px;width:57px;height:24px;background:linear-gradient(#4b9cd6,var(--btn-blue));border-radius:7px;color:#fff;font-size:10.5px;font-weight:700;text-align:center;line-height:24px}
.social{top:1054px;width:38px;height:38px;background:#3d6fb0;border-radius:3px}
.contact{right:68px;top:1053px;text-align:right;font-size:10px;line-height:17.8px;color:#ddd}
.partners{left:64px;top:1130px;width:571px;height:59px;background:#d9d9d9;display:flex;align-items:center;gap:8px;padding:0 2px}
.badge{height:53px;background:#9a9a9a}
.copyright{right:68px;top:1166px;font-size:9px;color:#ddd}
</style>
</head>
<body>

<header>
  <div class="abs greeting">Hello Guest!</div>
  <div class="abs account">Login<span>|</span>Register</div>
  <div class="abs brand">
    <div class="brand-name"><span class="brand-mark"></span>Stablemark Hire</div>
    <div class="brand-tag">Equestrian Recruitment Specialists</div>
  </div>
  <div class="abs promo">
    <div class="promo-main">Unbeatable Job Postings from just £30</div>
    <div class="promo-sponsor">Sponsored by<br>Saddlebrook Supplies</div>
    <div class="promo-strip">Now with over 1.9 million job views a week - you're in the right place</div>
  </div>
  <nav class="abs nav">
    <span class="current">Home</span><span class="sep">|</span>
    <span>About Us</span><span class="sep">|</span>
    <span>Employers</span><span class="sep">|</span>
    <span>Advertise</span><span class="sep">|</span>
    <span>News</span><span class="sep">|</span>
    <span>Resources</span>
  </nav>
</header>

<section class="abs hero">
  <svg class="abs hero-art" viewBox="0 0 894 348" role="img" aria-label="Soft light rays across a blue sky background">
    <polygon points="300,348 600,0 700,0 420,348" fill="#fff" opacity=".05"/>
    <polygon points="120,348 520,60 560,110 220,348" fill="#fff" opacity=".05"/>
    <ellipse cx="300" cy="240" rx="230" ry="70" fill="#fff" opacity=".05"/>
  </svg>
  <div class="abs welcome">Welcome to Stablemark Hire, your online resource for all Jobs within the Equestrian Industry. A simple, quick and efficient online tool to find a job and fill a position.</div>
  <div class="abs club-btn">VIEW OUR EXCLUSIVE SERVICE CLUB</div>
  <div class="abs search-title">Job Search</div>
  <div class="abs search-tabs">Job Type<span>|</span>Location</div>
  <div class="abs search-field">
    <svg width="32" height="32" viewBox="0 0 32 32"><circle cx="12" cy="12" r="9" fill="none" stroke="#999" stroke-width="3"/><line x1="18.5" y1="18.5" x2="29" y2="29" stroke="#888" stroke-width="5" stroke-linecap="round"/></svg>
    <span class="placeholder">Enter Keywords</span>
  </div>
  <div class="abs employer">I am an Employer looking for staff</div>
  <div class="abs show-all">Show all Jobs</div>
  <div class="abs search-btn">Search</div>
  <div class="abs adv-search">Advanced Search</div>
</section>

<div class="abs slider">
  <svg width="120" height="28" viewBox="0 0 120 28">
    <polyline points="18,9 13,14 18,19" fill="none" stroke="#555" stroke-width="2"/>
    <polyline points="102,9 107,14 102,19" fill="none" stroke="#555" stroke-width="2"/>
    <circle cx="38" cy="14" r="5" fill="#888" stroke="#666"/>
    <circle cx="53" cy="14" r="5" fill="#888"/>
    <circle cx="68" cy="14" r="5" fill="#888"/>
    <circle cx="83" cy="14" r="5" fill="#888"/>
  </svg>
</div>

<section>
  <h2 class="abs about-title">ABOUT US</h2>
  <div class="abs about-text">
    <p>Equestrian Jobs at StablemarkHire. A precise way for equine job seekers and employers to conduct a search for qualified candidates and jobs. No1 in Findwell and a reach of over 500,000 users in the UK alone. Now partnered with Listboard providing greater reach to the best talent in Europe.</p>
    <p>Equestrian Jobs at StablemarkHire. A precise way for equine job seekers and employers to conduct a search for qualified candidates and jobs. No1 in Findwell and a reach of over 500,000 users in the UK alone. Now partnered with Listboard providing greater reach to the best talent in Europe.</p>
  </div>
</section>

<section class="abs panels">
  <div class="abs divider" style="left:263px"></div>
  <div class="abs divider" style="left:509px"></div>

  <div class="abs" style="left:20px;top:24px;width:225px">
    <h2 class="col-title"><span class="hl">FEATURED</span> JOBS</h2>
    <div class="job"><h3>Groom/Assistant Instructor</h3><p>Mucking out, feeding, grooming, tacking up, medical, schooling, assist...</p></div>
    <div class="job"><h3>Groom/Rider</h3><p>To work on yard looking after competition horses and young horses</p></div>
    <div class="job" style="margin-top:9px"><h3>Horse Care Work</h3><p>HORSE CARE WORK-BASED DIPLOMA LEVEL 1, 2 and 3 These courses are suit...</p></div>
  </div>
  <div class="abs more" style="left:183px;top:231px">MORE</div>

  <div class="abs cv" style="left:287px;top:24px">
    <h2 class="col-title">CUREENT <span class="hl">CV</span></h2>
    <p>Lorem Ipsum is simply dummy text of the printing and typesetting industry. Lorem Ipsum has been the industry's standard dummy text ever since the 1500s, when an unknown printer dummy text ever since the 1500s, when an unknown printer.</p>
    <p>Lorem Ipsum is simply dummy text of the printing and typesetting industry. Lorem Ipsum has been the industry's standard dummy text ever since the 1500s, when an unknown printer dummy text ever since the 1500s, when an unknown printer.</p>
  </div>
  <div class="abs more" style="left:437px;top:231px">MORE</div>

  <div class="abs" style="left:530px;top:24px">
    <h2 class="col-title">CURRENT JOB <span class="hl">LISTINGS</span></h2>
    <ul class="listings">
      <li><svg width="10" height="10" viewBox="0 0 10 10"><polyline points="1,5 4,8 9,1" fill="none" stroke="#2d7fbf" stroke-width="2"/></svg>Job Position Name Comes Here</li>
      <li><svg width="10" height="10" viewBox="0 0 10 10"><polyline points="1,5 4,8 9,1" fill="none" stroke="#2d7fbf" stroke-width="2"/></svg>Job Position Name Comes Here</li>
      <li><svg width="10" height="10" viewBox="0 0 10 10"><polyline points="1,5 4,8 9,1" fill="none" stroke="#2d7fbf" stroke-width="2"/></svg>Job Position Name Comes Here</li>
      <li><svg width="10" height="10" viewBox="0 0 10 10"><polyline points="1,5 4,8 9,1" fill="none" stroke="#2d7fbf" stroke-width="2"/></svg>Job Position Name Comes Here</li>
      <li><svg width="10" height="10" viewBox="0 0 10 10"><polyline points="1,5 4,8 9,1" fill="none" stroke="#2d7fbf" stroke-width="2"/></svg>Job Position Name Comes Here</li>
      <li><svg width="10" height="10" viewBox="0 0 10 10"><polyline points="1,5 4,8 9,1" fill="none" stroke="#2d7fbf" stroke-width="2"/></svg>Job Position Name Comes Here</li>
      <li><svg width="10" height="10" viewBox="0 0 10 10"><polyline points="1,5 4,8 9,1" fill="none" stroke="#2d7fbf" stroke-width="2"/></svg>Job Position Name Comes Here</li>
    </ul>
  </div>
  <div class="abs more" style="left:670px;top:231px">MORE</div>
</section>

<footer>
  <div class="abs footer"></div>
  <div class="abs f-title" style="left:64px;top:989px">Current Job Listings</div>
  <ul class="abs f-links" style="left:64px;top:1015px">
    <li>Home</li><li>About Stablemark Hire</li><li>Equine Job Seekers</li><li>Equine Employers</li><li>Equine Industry News</li><li>\</li>
  </ul>
  <ul class="abs f-links" style="left:243px;top:1015px">
    <li>Webmasters</li><li>Current Job Listings</li><li>Equestrian Resources</li><li>Featured Jobs</li><li>How it Works</li>
  </ul>
  <ul class="abs f-links" style="left:414px;top:1015px">
    <li>Current Resume</li><li>Testimonials</li><li>Login</li><li>Register</li><li>Sitemap</li>
  </ul>
  <div class="abs f-title" style="left:592px;top:989px">Join Now</div>
  <div class="abs join-input"></div>
  <div class="abs signup">SIGN UP</div>
  <div class="abs social" style="left:592px"></div>
  <div class="abs social" style="left:645px;background:#4fb3e0"></div>
  <div class="abs contact">XXX City<br>XXX Street<br>Phone: xxx - xxx - xxx<br>Fax: xxx - xxx - xxx<br>info@website.com</div>
  <div class="abs partners">
    <div class="badge" style="width:40px;background:#eee"></div>
    <div class="badge" style="width:135px;background:#c8c8c8"></div>
    <div class="badge" style="width:42px;background:#eee"></div>
    <div class="badge" style="width:240px;background:#a8a8a8"></div>
    <div class="badge" style="width:58px;background:#555"></div>
  </div>
  <div class="abs copyright">© 2012. All Rights Reserved.</div>
</footer>

</body>
</html>
```